Business card for a "family office" company

Please provide professional looking business card designs, incorporating the attached logo and below details. Harrowmere Holdings Pty Ltd is a family office / financial investment company. We are looking for a modern, professional and contemporary card design.

Industry/Entity Type

Finance

Contact Information for Business Card

Name: Dean Mollick
Title: Director
Company: Harrowmere Holdings Pty Ltd
Email: harrowdean@quillnet.example
Mobile: 0462 735 418
Address: 4/312 Barnaby Parade, Cottesloe WA 6011, Australia

Requirements
Must have
• All details above and the logo. logo only on back side. incorporate colours of logo
Nice to have
• up to you
Should not have
• ?

```html
<!DOCTYPE html>
<html lang="en">
<head>
<meta charset="utf-8">
<title>Harrowmere Holdings – Business Card</title>
<link rel="stylesheet" href="https://fonts.googleapis.com/css2?family=PT+Sans:wght@400;700&display=swap">
<style>
  :root {
    --page-bg: #d9d6d2;
    --card-bg: #ebe8e4;
    --card-edge: #f6f4f1;
    --navy: #25233f;
    --band-text: #c9c2b8;
    --divider: #3a3852;
  }
  * { box-sizing: border-box; margin: 0; padding: 0; }
  html, body {
    width: 1200px; height: 969px; overflow: hidden;
    background: var(--page-bg);
    font-family: "PT Sans", Arial, sans-serif;
    color: var(--navy);
  }
  .card {
    position: absolute; left: 80px; top: 188px;
    width: 1040px; height: 592px;
    background: linear-gradient(160deg, var(--card-edge) 0%, var(--card-bg) 55%, #e2ded9 100%);
    border: 1px solid #f8f7f5;
    box-shadow: 0 18px 40px rgba(40, 35, 30, 0.18);
    overflow: hidden;
  }
  .brand {
    position: absolute; left: 60px; width: 420px; top: 200px;
    text-align: center;
  }
  .brand-mark {
    display: block; width: 60px; height: 60px; margin: 0 auto 26px;
    background: var(--navy);
  }
  .brand-name {
    font-weight: 700; font-size: 36px; letter-spacing: 3px;
    text-transform: uppercase; color: var(--navy); line-height: 1.1;
  }
  .divider {
    position: absolute; left: 552px; top: 156px;
    width: 2px; height: 270px; background: var(--divider);
  }
  .details { position: absolute; left: 597px; top: 150px; }
  .person-name { font-weight: 700; font-size: 26px; letter-spacing: 0.5px; text-transform: uppercase; line-height: 1.2; }
  .person-title { font-size: 26px; text-transform: uppercase; line-height: 1.2; margin-bottom: 22px; }
  .company { font-weight: 700; font-size: 24px; line-height: 1.35; }
  .address { font-size: 24px; line-height: 1.4; margin-bottom: 18px; }
  .contact { display: flex; align-items: center; gap: 14px; font-size: 24px; line-height: 1.4; }
  .contact svg { width: 18px; height: 18px; fill: var(--navy); flex: none; }
  .site-band {
    position: absolute; left: 0; bottom: 0; width: 100%; height: 50px;
    background: var(--navy);
  }
  .site-url {
    position: absolute; left: 0; width: 1040px; bottom: 8px;
    text-align: center; padding-right: 40px;
    color: var(--band-text); font-size: 25px; letter-spacing: 6px;
  }
  .corner-mark {
    position: absolute; right: 96px; bottom: 50px;
    width: 56px; height: 56px; background: var(--navy);
  }
</style>
</head>
<body>
  <div class="card">
    <div class="brand">
      <span class="brand-mark"></span>
      <div class="brand-name">Harrowmere<br>Holdings</div>
    </div>

    <div class="divider"></div>

    <div class="details">
      <div class="person-name">Dean Mollick</div>
      <div class="person-title">Director</div>
      <div class="company">Harrowmere Holdings Pty Ltd</div>
      <div class="address">4/312 Barnaby Parade<br>Cottesloe WA 6011, Australia</div>
      <div class="contact">
        <svg viewBox="0 0 18 18" aria-hidden="true"><path d="M5 1h8a1 1 0 0 1 1 1v14a1 1 0 0 1-1 1H5a1 1 0 0 1-1-1V2a1 1 0 0 1 1-1zm1 2v10h6V3z"/></svg>
        <span>0462 735 418</span>
      </div>
      <div class="contact">
        <svg viewBox="0 0 18 18" aria-hidden="true"><path d="M1 4h16v1.5L9 10 1 5.5z M1 7.3l8 4.5 8-4.5V14H1z"/></svg>
        <span>harrowdean@quillnet.example</span>
      </div>
    </div>

    <div class="corner-mark"></div>
    <div class="site-band"></div>
    <div class="site-url">harrowmereholdings.example</div>
  </div>
</body>
</html>
```